Time for a better IT consulting company?

We are a mobile computer consulting company, taking care of client's issues remotely or at their site. Website of company www.qr-lumotek.com. Business card is an example of marketing so far.
We moved this year but we still service our existing clients. We have expanded our number of technicians available. We would like to use this card for both new business and reaching out to old business.

Target Market(s)

This should target businesses and referrals to businesses from our existing clients as well as a new client outreach for our new location.

Industry/Entity Type

Computer

Requirements
Must have
• This postcard will let clients know we have moved into or we continue to service their area. Make sure it says Inc, not LLC. Must incorporate existing theme in some fashion.
Nice to have
• Themes to communicate: team of people standing by, stability, faster response time, accessibility.
• Areas of coverage: Westchester, Rockland, Manhattan, The Bronx, lower Connecticut.
Should not have
• Cartoon feel.

```html
<!DOCTYPE html>
<html lang="en">
<head>
<meta charset="utf-8">
<title>Lumotek Computer Consulting – Postcard</title>
<link rel="stylesheet" href="https://fonts.googleapis.com/css2?family=Archivo+Black&family=Arimo:wght@400;700&display=swap">
<style>
  :root {
    --ink: #111111;
    --body: #2b2b2b;
    --band: #3b3b3c;
    --brand-blue: #1aa3e2;
    --phone-grey: #3d3d3d;
    --white: #ffffff;
    --logo-grey: #4a4a4a;
  }
  * { margin: 0; padding: 0; box-sizing: border-box; }
  html, body { width: 1200px; height: 924px; overflow: hidden; background: var(--white); }
  .postcard {
    position: relative; width: 1200px; height: 924px; overflow: hidden;
    background: var(--white); font-family: "Arimo", Arial, sans-serif; color: var(--body);
  }
  .hero-photo {
    position: absolute; left: 560px; top: 0; width: 640px; height: 492px;
    background:
      linear-gradient(90deg, #ffffff 0%, rgba(255,255,255,0) 30%),
      linear-gradient(160deg, #eef4f9 0%, #c9d9e8 35%, #6f8fb0 60%, #2d4564 80%, #dfe8f0 100%);
  }
  .headline {
    position: absolute; left: 54px; top: 52px;
    font-family: "Archivo Black", "Arial Black", sans-serif;
    font-size: 44px; line-height: 55px; color: var(--ink); letter-spacing: 0.2px;
  }
  .intro {
    position: absolute; left: 54px; top: 231px;
    font-size: 24.5px; line-height: 29.5px; color: var(--body); white-space: nowrap;
  }
  .services-band {
    position: absolute; left: 0; top: 492px; width: 1200px; height: 246px; background: var(--band);
  }
  .services-tab {
    position: absolute; left: 58px; top: 474px; width: 326px; height: 47px;
    background: var(--brand-blue); color: var(--white);
    font-family: "Archivo Black", "Arial Black", sans-serif; font-size: 24px;
    line-height: 47px; padding-left: 22px; letter-spacing: 0.3px;
  }
  .service-list { position: absolute; top: 535px; list-style: none; }
  .service-list.col-a { left: 62px; }
  .service-list.col-b { left: 425px; }
  .service-list li {
    display: flex; align-items: center; height: 36.7px;
    font-size: 26.5px; color: var(--white);
  }
  .service-list svg { width: 26px; height: 26px; margin-right: 10px; flex: none; }
  .team-photo {
    position: absolute; left: 846px; top: 444px; width: 310px; height: 310px;
    border-radius: 50%; border: 9px solid var(--brand-blue);
    background: radial-gradient(circle at 60% 45%, #e7eef5 0%, #9fb2c6 40%, #44576d 80%, #2a3747 100%);
  }
  .brand { position: absolute; left: 70px; top: 762px; display: flex; align-items: center; }
  .brand-dot { width: 140px; height: 140px; border-radius: 50%; background: var(--logo-grey); flex: none; }
  .brand-name {
    margin-left: 18px; color: var(--logo-grey);
    font-family: "Arimo", Arial, sans-serif; font-weight: 700;
  }
  .brand-name .primary { display: block; font-size: 46px; line-height: 48px; letter-spacing: 1.5px; }
  .brand-name .secondary { display: block; font-size: 17px; letter-spacing: 5.4px; margin-top: 4px; }
  .contact { position: absolute; left: 700px; top: 772px; width: 470px; text-align: center; }
  .contact-label {
    font-family: "Arimo", Arial, sans-serif; font-weight: 700;
    font-size: 28px; color: var(--brand-blue); letter-spacing: 0.3px;
  }
  .contact-phone {
    font-family: "Arimo", Arial, sans-serif; font-weight: 700;
    font-size: 64px; line-height: 68px; color: var(--phone-grey); margin-top: 4px;
  }
  .contact-web {
    font-family: "Arimo", Arial, sans-serif; font-weight: 700;
    font-size: 23px; color: var(--phone-grey); margin-top: 2px;
  }
</style>
</head>
<body>
<main class="postcard">
  <div class="hero-photo" role="img" aria-label="Photo of three smiling office professionals giving a thumbs up beside a laptop and flip chart"></div>

  <h1 class="headline">NEED IMMEDIATE<br>ASSISTANCE WITH A<br>COMPUTER ISSUE?</h1>

  <p class="intro">For 18 years, my company provided<br>computer support to residents and<br>businesses in the Los Angeles area. At last<br>count, we had received 85 five star ratings<br>from our on-line clients. We have permanently<br>relocated to Westchester County and love its<br>charm. Now serving Westchester, Rockland,<br>Manhattan, The Bronx and lower Connecticut.</p>

  <section class="services-band" aria-label="Services offered"></section>
  <div class="services-tab">SERVICES OFFERED</div>

  <ul class="service-list col-a">
    <li><svg viewBox="0 0 26 26"><path d="M3 14 L10 21 L23 4" fill="none" stroke="#1aa3e2" stroke-width="3.2" stroke-linecap="round" stroke-linejoin="round"/></svg>Emergency Services</li>
    <li><svg viewBox="0 0 26 26"><path d="M3 14 L10 21 L23 4" fill="none" stroke="#1aa3e2" stroke-width="3.2" stroke-linecap="round" stroke-linejoin="round"/></svg>IT staffing</li>
    <li><svg viewBox="0 0 26 26"><path d="M3 14 L10 21 L23 4" fill="none" stroke="#1aa3e2" stroke-width="3.2" stroke-linecap="round" stroke-linejoin="round"/></svg>IP phones</li>
    <li><svg viewBox="0 0 26 26"><path d="M3 14 L10 21 L23 4" fill="none" stroke="#1aa3e2" stroke-width="3.2" stroke-linecap="round" stroke-linejoin="round"/></svg>Hardware/Software</li>
    <li><svg viewBox="0 0 26 26"><path d="M3 14 L10 21 L23 4" fill="none" stroke="#1aa3e2" stroke-width="3.2" stroke-linecap="round" stroke-linejoin="round"/></svg>Security Reviews</li>
  </ul>
  <ul class="service-list col-b">
    <li><svg viewBox="0 0 26 26"><path d="M3 14 L10 21 L23 4" fill="none" stroke="#1aa3e2" stroke-width="3.2" stroke-linecap="round" stroke-linejoin="round"/></svg>Emergency Services</li>
    <li><svg viewBox="0 0 26 26"><path d="M3 14 L10 21 L23 4" fill="none" stroke="#1aa3e2" stroke-width="3.2" stroke-linecap="round" stroke-linejoin="round"/></svg>IT staffing</li>
    <li><svg viewBox="0 0 26 26"><path d="M3 14 L10 21 L23 4" fill="none" stroke="#1aa3e2" stroke-width="3.2" stroke-linecap="round" stroke-linejoin="round"/></svg>IP phones</li>
    <li><svg viewBox="0 0 26 26"><path d="M3 14 L10 21 L23 4" fill="none" stroke="#1aa3e2" stroke-width="3.2" stroke-linecap="round" stroke-linejoin="round"/></svg>Hardware/Software</li>
    <li><svg viewBox="0 0 26 26"><path d="M3 14 L10 21 L23 4" fill="none" stroke="#1aa3e2" stroke-width="3.2" stroke-linecap="round" stroke-linejoin="round"/></svg>Security Reviews</li>
  </ul>

  <div class="team-photo" role="img" aria-label="Photo of two technicians reviewing a laptop in a server room"></div>

  <div class="brand">
    <div class="brand-dot"></div>
    <div class="brand-name">
      <span class="primary">LUMOTEK</span>
      <span class="secondary">COMPUTER CONSULTING, INC</span>
    </div>
  </div>

  <div class="contact">
    <p class="contact-label">GET CONNECT WITH US:</p>
    <p class="contact-phone">914-555-0172</p>
    <p class="contact-web">www.qr-lumotek.com</p>
  </div>
</main>
</body>
</html>
```